Film Poster

The poster is for a small short comedy film which we are sending to Festivals and hoping it gets picked up as a tv series and we do have a few interested parties who are waiting on the final cut of the film to then decide if they want to commission more episodes. The poster would be used throughout all advertising globally and we would promote you on a regular bases via social media of the film and website etc.
The Brief:
The poster needs to be in a professional format of a movie film poster. Please make sure you understand the presentation of a film poster.
Image attached which we would like to use on the poster (running image). Possibly using just the character cut out of the image and placed on a different background. Alternatively, you can redo an old poster which features the same character, this is also attached. I have also uploaded a few other stills that you can choose to work with.
There needs to be various text on the poster;
Title: Pike and the Dancer
Tagline: When a fresh start leaves you stranded.
Credit Block:
A Tilvern Films production Written and Directed by Hal Mergate Oduya Producer Hal Mergate Oduya Co-Producer Delphine Aswick Director of Photography Teodor Kivrashen
Updates
Hi everyone,
I just want to inform you all that we have now changed this project to "payment committed". A huge thank you to everyone for your fantastic submissions and for those of you who have taken our feedback on board. We are really pleased with the standard which is why we have now committed to payment. It will be a tough final decision for us, but we welcome you all to make our decision the hardest possible by submitting excellent designs. Whoever we choose to go with, there will certainly be a few more of you who we would love to keep in contact with afterwards regarding future work we may have for you so do feel free to direct us to other locations such as a website you may have where we can see more of your work and also any other contact details you would like us to have so we can keep you on our database.
Many thanks again to all of you for your continued efforts and best of luck to everyone! Any questions, please don't hesitate to contact me and I will get back to you as soon as I can.
Kind Regards,
Delphine.
Can we please see the following credit block on the poster? Many Thanks, Delphine.
A Tilvern Films Production Hal Mergate Oduya "Pike and the Dancer" Harriet Olund Wren Cortley-Yusef Gideon Tulk Valeria Skjorn Mira Josko Tilly Ferne Joanne Pettigrall and Rosalind Dunhoe Music by... ? Director of Photography Teodor Kivrashen Producer Hal Mergate Oduya Co-Producer Delphine Aswick Written and Directed by Hal Mergate Oduya

```html
<!DOCTYPE html>
<html lang="en">
<head>
<meta charset="utf-8">
<title>Pike and the Dancer — Poster</title>
<link rel="stylesheet" href="https://fonts.googleapis.com/css2?family=Ubuntu:wght@400;500&display=swap">
<style>
  :root {
    --ink: #000000;
    --accent: #f6e61a;
    --photo-light: #8a8a8a;
    --photo-mid: #4a4a4a;
    --photo-low: #2a2a2a;
    --photo-dark: #0b0b0b;
  }
  html, body {
    margin: 0;
    padding: 0;
    width: 840px;
    height: 1200px;
    overflow: hidden;
    background: var(--ink);
  }
  .poster {
    position: relative;
    width: 840px;
    height: 1200px;
    background: var(--ink);
    overflow: hidden;
    font-family: "Ubuntu", sans-serif;
    color: var(--accent);
  }
  .poster__photo {
    position: absolute;
    inset: 0;
    background:
      radial-gradient(ellipse 230px 120px at 470px 170px, var(--photo-mid) 0%, var(--photo-low) 70%, transparent 100%),
      radial-gradient(ellipse 230px 300px at 420px 420px, var(--photo-light) 0%, var(--photo-mid) 55%, transparent 100%),
      radial-gradient(ellipse 520px 520px at 420px 960px, var(--photo-mid) 0%, var(--photo-low) 55%, transparent 100%),
      radial-gradient(ellipse 140px 200px at 770px 860px, var(--photo-mid) 0%, transparent 100%),
      var(--photo-dark);
  }
  .poster__tagline {
    position: absolute;
    top: 30px;
    left: 0;
    width: 840px;
    margin: 0;
    text-align: center;
    font-size: 30px;
    font-weight: 500;
    letter-spacing: 1px;
    text-transform: uppercase;
  }
  .poster__title {
    position: absolute;
    left: 0;
    top: 0;
    margin: 0;
    font-weight: 400;
    text-transform: uppercase;
    line-height: 1;
  }
  .title__line {
    position: absolute;
    white-space: nowrap;
  }
  .title__line--first { left: 24px;  top: 548px; font-size: 134px; }
  .title__line--and   { left: 88px;  top: 678px; font-size: 82px; }
  .title__line--the   { left: 180px; top: 766px; font-size: 82px; }
  .title__line--last  { left: 24px;  top: 840px; font-size: 112px; }
  .poster__cast {
    position: absolute;
    left: 0;
    top: 1010px;
    width: 840px;
    margin: 0;
    text-align: center;
    line-height: 1;
  }
  .poster__credits {
    position: absolute;
    left: 0;
    top: 1082px;
    width: 840px;
    margin: 0;
    text-align: center;
    line-height: 1;
  }
  .credits__row {
    display: block;
    margin-bottom: 8px;
    white-space: nowrap;
  }
  .credits__label { font-size: 13px; }
  .credits__name  { font-size: 19px; }
  .credits__sep   { font-size: 17px; margin: 0 6px; }
</style>
</head>
<body>
  <main class="poster">
    <div class="poster__photo" role="img" aria-label="Black and white portrait of the lead character in a flat cap, glasses and scarf, with a scratched film texture, filling the poster"></div>

    <p class="poster__tagline">When a fresh start leaves you stranded.</p>

    <h1 class="poster__title">
      <span class="title__line title__line--first">Pike</span>
      <span class="title__line title__line--and">and</span>
      <span class="title__line title__line--the">the</span>
      <span class="title__line title__line--last">Dancer</span>
    </h1>

    <p class="poster__cast">
      <span class="credits__row">
        <span class="credits__label">A Tilvern Films Production</span> <span class="credits__name">Hal Mergate Oduya</span> <span class="credits__label">“Pike and the Dancer”</span>
      </span>
      <span class="credits__row">
        <span class="credits__name">Harriet Olund · Wren Cortley-Yusef · Gideon Tulk · Valeria Skjorn</span>
      </span>
      <span class="credits__row">
        <span class="credits__name">Mira Josko · Tilly Ferne · Joanne Pettigrall</span> <span class="credits__label">and</span> <span class="credits__name">Rosalind Dunhoe</span>
      </span>
    </p>

    <p class="poster__credits">
      <span class="credits__row">
        <span class="credits__name">A Tilvern Films</span> <span class="credits__label">Production</span>
        <span class="credits__sep">|</span>
        <span class="credits__label">Written and Directed by</span> <span class="credits__name">Hal Mergate Oduya</span>
      </span>
      <span class="credits__row">
        <span class="credits__label">Producer</span> <span class="credits__name">Hal Mergate Oduya</span>
        <span class="credits__sep">|</span>
        <span class="credits__label">Co-Producer</span> <span class="credits__name">Delphine Aswick</span>
      </span>
      <span class="credits__row">
        <span class="credits__label">Director of Photography</span> <span class="credits__name">Teodor Kivrashen</span>
      </span>
    </p>
  </main>
</body>
</html>
```